VoltNest EV Charger Installation

We are an electrical contractor "Brannock Electric" http://brannockelectricworks.example.

New site is for a division we are creating. http://voltnestelectric.example/ is registered on Google domains.
Company is registered as VoltNest LLC.
VoltNest is something we are trying out to see if we can find a niche installing EV chargers and EV Charger outlets in existing homes and businesses. Looking to work it as a division off from Brannock Electric short term and if successful it would become a stand alone business. Often times this requires additional work to meet code. Work such as adding smoke & carbon monoxide detectors, new electrical panels and upgrading the electrical Main Service Meter system.
Will need to coordinate this site with our current Brannock Electric website. Not sure how this can work. We like the look of our current Brannock Electric Wordpress site, but it is dated and broken, in need of a rebuild or repair as well.
Need a website as a landing point for Google Maps inquiries and possibly as a way to drive customers to call for our services. Need to be mindful that we want to avoid confusion with people looking for EV charger Stations to drive and plug in their cars. We are a contractor not a place to plug in! The name may be problematic in this sense.
Looking for a site that coordinates style & color with the provided VoltNest logo. Would like to have a contact / inquiry page with a captcha or similar tool to weed out spam. need to integrate google maps and similar tools to measure marketing, assist in lead generation, etc.
Have Logo artwork. Not sure what format is best to upload.

Target Market(s)

People with electric cars, business owners and homeowners.

Industry/Entity Type

Electrical Contractor- Residential & Light Commercial (mostly residential)

Requirements
Must have
• Landing Page/about us , Contact Us/ inquiry Page with a quality captcha filter, Job Gallery- we don't have many pics yet. Google pointers /tools. Open to suggestions here! Mobile Phone/ Tablet friendly is important. I listed coded design but not quite sure what that means.
Nice to have
• Similar to the Brannock Electric site style a possibility, but open to suggestions. Possibly have something that shows the business is connected to Brannock Electric? ..."A division of Brannock Electric" with logo/link to site?

```html
<!DOCTYPE html>
<html lang="en">
<head>
<meta charset="utf-8">
<title>VoltNest – EV Charger Installation</title>
<link href="https://fonts.googleapis.com/css2?family=Inter:wght@400;500;600;700&display=swap" rel="stylesheet">
<style>
:root{
  --green:#7fbf3a;
  --green-btn:#82c341;
  --nav:#2b2b2b;
  --ink:#1c1c1c;
  --grey-band:#d9d9d9;
  --grey-sec:#efefef;
  --footer:#121212;
  --legal:#3a3a3a;
  --white:#ffffff;
  --brand-red:#d9262c;
}
*{box-sizing:border-box;margin:0;padding:0}
html,body{width:1200px;height:2943px;overflow:hidden}
body{font-family:'Inter',sans-serif;color:var(--ink);background:var(--white);position:relative}
.abs{position:absolute}
section,header,nav,footer{position:absolute;left:0;width:1200px}
.btn{position:absolute;display:flex;align-items:center;justify-content:center;background:var(--green-btn);color:#fff;border:2px solid #fff;border-radius:8px;font-size:14px;font-weight:500;letter-spacing:.3px;text-transform:uppercase}
.brand{display:flex;align-items:center;gap:10px;font-weight:700;letter-spacing:.5px}
.brand .dot{width:26px;height:26px;border-radius:50%;background:var(--green)}
.photo{position:absolute}

/* top bar */
.topbar{top:0;height:26px;background:var(--green);color:#fff;font-size:13px;font-weight:500}
.topbar .division{left:131px;top:0;height:26px;display:flex;align-items:center;gap:10px}
.topbar .mini-btn{height:17px;padding:0 9px;border:1px solid #fff;font-size:11px;font-weight:400;display:flex;align-items:center;justify-content:center}
.topbar .phone{right:131px;top:5px;display:flex;align-items:center;gap:6px;font-size:12px}
.topbar .phone i{width:16px;height:16px;border-radius:50%;background:#fff;display:flex;align-items:center;justify-content:center}

/* nav */
.nav{top:26px;height:92px;background:var(--nav)}
.nav .brand{left:134px;top:31px;color:#fff;font-size:24px}
.nav .link{top:38px;color:#fff;font-size:14px;font-weight:500}
.nav .btn{left:922px;top:24px;width:155px;height:44px}

/* hero */
.hero{top:118px;height:549px;background:linear-gradient(100deg,#3f3d3b 0%,#6f7077 30%,#8c8e96 55%,#b8bcc4 75%,#6e7078 100%)}
.hero h1{position:absolute;left:128px;top:124px;color:#fff;font-size:56px;font-weight:600;line-height:64px;letter-spacing:-.5px}
.hero p{position:absolute;left:128px;top:259px;color:#fff;font-size:20px;line-height:25px}
.hero .btn{left:126px;top:333px;width:154px;height:44px}
.arrow{position:absolute;width:41px;height:42px;background:#fff;display:flex;align-items:center;justify-content:center}
.hero .prev{left:49px;top:248px}
.hero .next{left:1077px;top:248px}
.dots{position:absolute;left:580px;top:492px;display:flex;gap:6px}
.dots span{width:9px;height:9px;border-radius:50%;background:#ddd}
.dots span:first-child{background:var(--green)}

/* division band */
.division-band{top:667px;height:77px;background:var(--grey-band)}
.division-row{position:absolute;left:0;width:1200px;top:20px;height:35px;display:flex;align-items:center;justify-content:center;gap:14px}
.division-row .label{font-size:20px;font-weight:500}
.division-row .parent{font-size:20px;font-weight:700;color:var(--brand-red)}
.division-row .band-btn{height:35px;width:106px;display:flex;align-items:center;justify-content:center;background:var(--green-btn);color:#fff;border:2px solid #fff;font-size:12px;font-weight:500}

/* about */
.about{top:744px;height:632px}
.about .main-photo{left:106px;top:111px;width:364px;height:418px;background:linear-gradient(135deg,#eceae3,#c9c8c3 60%,#8a8b8d);clip-path:polygon(0 0,100% 0,100% 47%,62.9% 47%,62.9% 100%,0 100%)}
.about .side-photo{left:381px;top:325px;width:197px;height:232px;background:linear-gradient(180deg,#f1f1f1,#b9b9b4 55%,#6e7a68)}
.about .brand{left:618px;top:128px;font-size:24px;color:var(--ink)}
.about h2{position:absolute;left:627px;top:180px;font-size:27px;font-weight:600;letter-spacing:-.2px}
.about .copy{position:absolute;left:630px;top:247px;width:455px;font-size:13px;line-height:20px}
.about .copy p+p{margin-top:20px}
.about .btn{left:637px;top:527px;width:153px;height:43px;border:none}

/* cost */
.cost{top:1376px;height:511px;background:var(--grey-sec)}
.cost .copy{position:absolute;left:125px;top:101px;width:430px;font-size:13px;line-height:20px}
.cost .copy p+p{margin-top:20px}
.cost .permit{position:absolute;left:128px;top:291px;font-size:20px;font-weight:600;line-height:30px}
.cost .frame{left:642px;top:62px;width:429px;height:387px;background:#fff}
.cost .panel-photo{left:658px;top:79px;width:397px;height:353px;background:linear-gradient(180deg,#b8a58a,#d8c6a6 40%,#cfc0a2 70%,#8a8070)}

/* contact cta */
.cta{top:1887px;height:411px;background:linear-gradient(180deg,rgba(120,176,58,.92),rgba(104,160,52,.92)),linear-gradient(90deg,#8aa070,#c8d6b0 50%,#7e9466)}
.cta h2{position:absolute;left:0;width:1136px;text-align:center;top:108px;color:#fff;font-size:35px;font-weight:500}
.cta p{position:absolute;left:0;width:1170px;text-align:center;top:155px;color:#fff;font-size:20px;font-weight:500;line-height:30px}
.cta .btn{left:522px;top:238px;width:155px;height:43px}

/* gallery */
.gallery{top:2298px;height:447px}
.gallery h2{position:absolute;left:0;width:1136px;text-align:center;top:58px;font-size:27px;font-weight:700}
.gallery .photo{top:136px;height:220px;width:221px}
.g1{left:139px;background:linear-gradient(180deg,#eef0ee,#c9cbc8)}
.g2{left:375px;background:linear-gradient(180deg,#d8d4cc,#7a5e40)}
.g3{left:610px;background:linear-gradient(180deg,#6b7a4e,#a6774c 60%,#8e6a48)}
.g4{left:846px;background:linear-gradient(180deg,#f0f0ef,#8e9c86 60%,#e8e8e6)}
.gallery .arrow{background:var(--green-btn);top:229px}
.gallery .prev{left:119px}
.gallery .next{left:1045px}

/* footer */
.site-footer{top:2745px;height:165px;background:var(--footer);color:#fff}
.site-footer .brand{left:145px;top:52px;font-size:24px}
.site-footer h4{position:absolute;top:50px;font-size:14px;font-weight:500}
.site-footer .col{position:absolute;font-size:13px;line-height:24px}
.contact-col{left:465px;top:72px}
.contact-col div{display:flex;align-items:center;gap:6px}
.contact-col i{width:17px;height:17px;border-radius:50%;background:var(--green);display:flex;align-items:center;justify-content:center}
.links-col{left:711px;top:74px;font-size:12px;line-height:20px}
.site-footer .div-label{left:931px;top:45px;font-size:17px;font-weight:500}
.site-footer .parent{left:899px;top:78px;font-size:22px;font-weight:700;color:var(--brand-red)}
.legal{left:0;width:1200px;top:2910px;height:33px;background:var(--legal);color:#e0e0e0;font-size:10px;text-align:center;line-height:33px}
</style>
</head>
<body>

<header class="topbar">
  <div class="abs division"><span>A division of Brannock Electric"</span><span class="mini-btn">Click Here</span></div>
  <div class="abs phone"><i><svg width="10" height="10" viewBox="0 0 24 24"><path fill="#7fbf3a" d="M6.6 10.8a15 15 0 0 0 6.6 6.6l2.2-2.2a1 1 0 0 1 1-.25 11.4 11.4 0 0 0 3.6.57 1 1 0 0 1 1 1V20a1 1 0 0 1-1 1A17 17 0 0 1 3 4a1 1 0 0 1 1-1h3.5a1 1 0 0 1 1 1c0 1.25.2 2.45.57 3.57a1 1 0 0 1-.25 1z"/></svg></i>555.201.4830</div>
</header>

<nav class="nav">
  <div class="abs brand"><span class="dot"></span>VoltNest</div>
  <div class="abs link" style="left:689px">ABOUT US</div>
  <div class="abs link" style="left:800px">CONTACT US</div>
  <div class="btn">Get in touch</div>
</nav>

<section class="hero" role="img" aria-label="Woman plugging a charger into a white electric car outside a home">
  <h1>Need an electric<br>car charger?</h1>
  <p>Electric vehicles (EVs) are here.<br>Let VoltNest help you get powered up!</p>
  <div class="btn">Get in touch</div>
  <div class="arrow prev"><svg width="14" height="24" viewBox="0 0 14 24"><path d="M12 2 2 12l10 10" fill="none" stroke="#7fbf3a" stroke-width="2"/></svg></div>
  <div class="arrow next"><svg width="14" height="24" viewBox="0 0 14 24"><path d="M2 2l10 10L2 22" fill="none" stroke="#7fbf3a" stroke-width="2"/></svg></div>
  <div class="dots"><span></span><span></span><span></span></div>
</section>

<section class="division-band">
  <div class="division-row">
    <span class="label">A division of</span>
    <span class="parent">Brannock Electric</span>
    <span class="band-btn">Click Here</span>
  </div>
</section>

<section class="about">
  <div class="photo main-photo" role="img" aria-label="White electric SUV parked in a garage beside a wall-mounted charger"></div>
  <div class="photo side-photo" role="img" aria-label="Bright living room with ceiling fan and large windows"></div>
  <div class="abs brand"><span class="dot"></span>VoltNest</div>
  <h2>Ev Chatging Installation Services</h2>
  <div class="copy">
    <p>EV charger installation is a relatively simple process, but it's important to hire a qualified electrician. VoltNest is a division of Brannock Electric, a licensed and insured electrical contractor. We are committed to providing our customers with a quality, code approved installation.</p>
    <p>We'll assess your home's electrical system and help find a safe and convenient location for the charger or charger outlet. In some cases, a homeor business electrical panel or Main electrical service system may require an upgrade to accommodate adding an EV charger(s). Additionally, some jurisdictions require that a home's smoke detectors be brought up to current code standards. We can help you determine if any upgrades are necessary and can provide you with a quote for the work.</p>
  </div>
  <div class="btn">Get in touch</div>
</section>

<section class="cost">
  <div class="copy">
    <p>The cost of EV charger installation will vary depending on a number of factors, including the type of charger, the distance and access to the electrical panel. Typical charger installations range from <strong>$600 to $2,000.</strong></p>
    <p>Once your EV charger is installed, you'll start enjoying the convenience of at-<br>home/business charging and the many benefits of owning an EV.</p>
  </div>
  <div class="permit">VoltNest will acquire the required<br>electrical permit for your job.</div>
  <div class="photo frame"></div>
  <div class="photo panel-photo" role="img" aria-label="Electrical panels and a home battery unit mounted on a plywood wall"></div>
</section>

<section class="cta" role="img" aria-label="Open-plan living room and kitchen under a green tint">
  <h2>Contact VoltNest Today</h2>
  <p>We look forward to discussing your EV charger<br>installation evaluation and &nbsp;estimate.</p>
  <div class="btn">Get in touch</div>
</section>

<section class="gallery">
  <h2>PROJECTS GALLERY</h2>
  <div class="photo g1" role="img" aria-label="Open electrical breaker panel"></div>
  <div class="photo g2" role="img" aria-label="Kitchen with island and bar stools"></div>
  <div class="photo g3" role="img" aria-label="Outdoor service meter mounted on a wooden post"></div>
  <div class="photo g4" role="img" aria-label="Bright sunroom with ceiling fan"></div>
  <div class="arrow prev"><svg width="14" height="24" viewBox="0 0 14 24"><path d="M12 2 2 12l10 10" fill="none" stroke="#fff" stroke-width="2"/></svg></div>
  <div class="arrow next"><svg width="14" height="24" viewBox="0 0 14 24"><path d="M2 2l10 10L2 22" fill="none" stroke="#fff" stroke-width="2"/></svg></div>
</section>

<footer class="site-footer">
  <div class="abs brand"><span class="dot"></span>VoltNest</div>
  <h4 style="left:465px">CONTACT INFORMATION</h4>
  <div class="col contact-col">
    <div><i><svg width="10" height="10" viewBox="0 0 24 24"><path fill="#fff" d="M6.6 10.8a15 15 0 0 0 6.6 6.6l2.2-2.2a1 1 0 0 1 1-.25 11.4 11.4 0 0 0 3.6.57 1 1 0 0 1 1 1V20a1 1 0 0 1-1 1A17 17 0 0 1 3 4a1 1 0 0 1 1-1h3.5a1 1 0 0 1 1 1c0 1.25.2 2.45.57 3.57a1 1 0 0 1-.25 1z"/></svg></i>555.201.4830</div>
    <div><i><svg width="10" height="10" viewBox="0 0 24 24"><path fill="none" stroke="#fff" stroke-width="2.5" d="M3 6h18v12H3zM3 6l9 7 9-7"/></svg></i>info@voltnest.example</div>
  </div>
  <h4 style="left:709px">QUICKLINKS</h4>
  <div class="col links-col">About us<br>Contact us</div>
  <div class="abs div-label">A division of</div>
  <div class="abs parent">Brannock Electric</div>
</footer>

<div class="abs legal">© Copyright 2023 Brannock Electric | All Rights Reserved</div>

</body>
</html>
```